Custom Home Builder needs a Company Brochure

We need a brochure designed for our custom built building company in the Whitsundays QLD, Australia.
We are a young, fresh building company that offers clients a custom building process with outstanding quality and communication.

We would like to see designs that portray our innovative, modern culture and incorporate our company colours of bright blue, grey and white.

We don't want the brochure to be too formal, but it must flow from start to finish and be an easy to read brochure.

Our website is www.Q85homes.com.au

I have other lifestyle images that I would like to add, but they are large files and I am not able to upload them to this website. I have a dropbox link with all photos https://www.filecrate.net/sh/xk3vbn7wq21pq4z/QRTmPz8_vnsYtkLqWpHdGcXeRa?dl=0

I have added a photo of our work vehicle which has a style of design that I like, with the curved lines etc.

Target Market(s)

2nd and 3rd New Home owners wanting to build a quality custom designed home

Industry/Entity Type

Home Builder

Font styles to use
Sans Serif

Colors
0792cd
7f7f7f
ffffff
000000

Requirements
Must have
• A4
• Prefer portrait layout
• Creative, modern, fresh feel to the brochure
Nice to have
• I like to see soft lines rather than sharp straight lines
• Curves, waves, circles etc.

```html
<!DOCTYPE html>
<html lang="en">
<head>
<meta charset="utf-8">
<title>Why Build With Quay 85 Homes – Brochure Spread</title>
<link rel="stylesheet" href="https://fonts.googleapis.com/css2?family=Montserrat:wght@600;700&family=Open+Sans:wght@400;600&family=Lora:ital@1&display=swap">
<style>
  :root{
    --blue:#0792cd;
    --grey:#7f7f7f;
    --dark:#3d3f42;
    --bar-dark:#55585c;
    --text:#4a4a4a;
    --paper:#ffffff;
    --stage:#e6e7e9;
    --rule:#9a9a9a;
    --seal:#5a8db0;
  }
  *{box-sizing:border-box;margin:0;padding:0}
  html,body{width:1200px;height:789px;overflow:hidden;background:var(--stage)}
  body{font-family:"Open Sans",Arial,sans-serif;color:var(--text);position:relative}
  .spread{position:absolute;left:63px;top:14px;width:1074px;height:760px;display:flex;box-shadow:0 6px 24px rgba(0,0,0,.18)}
  .page{position:relative;width:537px;height:760px;background:var(--paper);overflow:hidden}
  .page--left{background:linear-gradient(90deg,#fff 85%,#eceef0 100%)}
  .page--right{background:linear-gradient(90deg,#eceef0 0%,#fff 12%)}

  .title{position:absolute;font-family:"Montserrat",Arial,sans-serif;font-weight:700;font-size:34px;letter-spacing:1px;color:var(--dark);white-space:nowrap}
  .title--left{right:18px;top:58px}
  .title--right{left:18px;top:58px}
  .title .accent{color:var(--blue)}
  .title-rule{position:absolute;top:102px;height:2px;background:var(--rule)}
  .page--left .title-rule{left:150px;right:0}
  .page--right .title-rule{left:0;right:30px}

  .feature{position:absolute;width:150px}
  .feature__head{display:flex;align-items:center;height:34px}
  .feature__num{font-family:"Montserrat",Arial,sans-serif;font-weight:600;font-size:52px;line-height:1;color:var(--dark);margin-right:-6px;position:relative;z-index:1}
  .feature__bar{flex:1;min-height:22px;display:flex;align-items:center;padding:3px 8px;font-size:9px;line-height:1.2;color:#fff;background:var(--blue)}
  .feature__bar--dark{background:var(--bar-dark)}
  .feature__body{margin-top:16px;font-size:9px;line-height:1.42;text-align:justify}
  .feature__body p+p{margin-top:10px}

  .photo{position:absolute}
  .photo--worker{left:20px;top:440px;width:200px;height:190px;background:linear-gradient(160deg,#dfe8ef,#a9b8c5 60%,#7d8c62)}
  .photo--meeting{left:190px;top:560px;width:190px;height:150px;background:linear-gradient(135deg,#2d3138,#a6a9ae 55%,#e3dcd4)}
  .photo--kitchen{left:395px;top:420px;width:142px;height:300px;background:linear-gradient(180deg,#d9d4cb,#b39d80 55%,#6f6a64)}
  .photo--couple{left:40px;top:455px;width:130px;height:95px;background:linear-gradient(135deg,#c9b49c,#e9e2d8 55%,#8fa0b3)}
  .photo--award{left:180px;top:470px;width:150px;height:105px;background:linear-gradient(135deg,#1f2428,#6d7176 55%,#b9a46a)}

  .seal{position:absolute;left:440px;top:485px;width:56px;height:56px;border-radius:50%;background:var(--seal)}

  .quote{position:absolute;left:40px;top:588px;width:460px;height:124px;border:1.5px solid #c9cbce;border-radius:14px;padding:14px 30px 0;text-align:center;font-size:10.5px;line-height:1.45;color:var(--text)}
  .quote__mark{position:absolute;font-family:"Montserrat",Arial,sans-serif;font-weight:700;font-size:30px;color:var(--blue);line-height:1}
  .quote__mark--open{left:8px;top:-12px}
  .quote__mark--close{right:8px;bottom:-20px}
  .quote__by{position:absolute;right:44px;bottom:8px;font-family:"Lora",Georgia,serif;font-style:italic;font-size:12px;line-height:1;color:var(--dark)}

  .footer-band{position:absolute;left:0;right:0;bottom:0;height:38px;background:var(--grey);display:flex;align-items:center;justify-content:flex-end;padding-right:28px}
  .footer-band__web{font-size:16px;letter-spacing:1px;color:#fff}
</style>
</head>
<body>
<main class="spread">

  <section class="page page--left" aria-label="Page 2">
    <h1 class="title title--left">WHY BUILD WITH</h1>
    <div class="title-rule"></div>

    <article class="feature" style="left:20px;top:130px">
      <div class="feature__head"><span class="feature__num">1</span><span class="feature__bar">Project Management</span></div>
      <div class="feature__body"><p>We have an online project management system which is second to none, and utilized the latest in estimating and job management software. Each individual project is managed online so our clients are up to date with the progress of their new home at all times, giving them clarity and re-assurance through-out the entire project.</p></div>
    </article>

    <article class="feature" style="left:190px;top:170px;width:170px">
      <div class="feature__head"><span class="feature__num">2</span><span class="feature__bar feature__bar--dark">Exceptional Customer Care and Superior Communication</span></div>
      <div class="feature__body">
        <p>Our exceptional service and communication ensures that your building experience is an enjoyable and worry free experience.</p>
        <p>We communicate with you through our online project management system so you will feel like part of the team and will be kept up to date on all progress, budgets and selections.</p>
        <p>All of this is clearly documented throughout the building process guaranteeing that we can eliminate 100% of selection mistakes by keeping our lines of communication to the highest possible level.</p>
      </div>
    </article>

    <article class="feature" style="left:375px;top:210px;width:145px">
      <div class="feature__head"><span class="feature__num">3</span><span class="feature__bar">Quality Finishes</span></div>
      <div class="feature__body"><p>Our high level of technical expertise and attention to detail ensures that all of your expectations and requirements will not only be met but exceeded.</p></div>
    </article>

    <div class="photo photo--worker" role="img" aria-label="Photo of a builder in hard hat and hi-vis vest reviewing plans"></div>
    <div class="photo photo--meeting" role="img" aria-label="Photo of clients meeting with a consultant"></div>
    <div class="photo photo--kitchen" role="img" aria-label="Photo of a modern kitchen with stainless steel oven"></div>
  </section>

  <section class="page page--right" aria-label="Page 3">
    <h2 class="title title--right"><span class="accent">QUAY 85</span> HOMES?</h2>
    <div class="title-rule"></div>

    <article class="feature" style="left:18px;top:130px;width:150px">
      <div class="feature__head"><span class="feature__num">4</span><span class="feature__bar">Personal Attention</span></div>
      <div class="feature__body">
        <p>You will receive personal attention from our director Daniel Corwen, to ensure that your home is built to the standard and quality that you expect.</p>
        <p>You will receive regular site meetings so you can experience first hand and contribute to discussions on any current issues.</p>
      </div>
    </article>

    <article class="feature" style="left:185px;top:165px;width:160px">
      <div class="feature__head"><span class="feature__num">5</span><span class="feature__bar feature__bar--dark">Professional Team</span></div>
      <div class="feature__body">
        <p>We only employ a highly skilled team of carpenters and sub-contractors that are experienced in the construction of quality new homes.</p>
        <p>Our membership with Coastal Builders Guild ensures that we stay up to date with the latest industry standards, which guarantees that your home is built with exceptional quality, giving you a finish of un-paralleled quality.</p>
      </div>
    </article>

    <article class="feature" style="left:362px;top:200px;width:155px">
      <div class="feature__head"><span class="feature__num">6</span><span class="feature__bar">Quality Assurance</span></div>
      <div class="feature__body">
        <p>Every new home undergoes our minimum 250 point Quality Assurance Check list to ensure that even the smallest details are examined and rectified before you move into your new home.</p>
        <p>We want to give you complete piece of mind knowing that your home will be built and finished to the highest possible standard.</p>
      </div>
    </article>

    <div class="photo photo--couple" role="img" aria-label="Photo of a happy couple in their new home"></div>
    <div class="photo photo--award" role="img" aria-label="Photo of the team receiving an industry award"></div>

    <div class="seal" role="img" aria-label="Satisfaction guarantee seal"></div>

    <blockquote class="quote">
      <span class="quote__mark quote__mark--open">&ldquo;</span>
      We are so happy we chose you to build our house. Tess and Daniel were an amazing team to work with.<br>
      They went out of their way to ensure our house was perfect and exactly what we wanted, we can never thank them enough.<br>
      Both Mark &amp; I would recommend their team to anyone.
      <span class="quote__by">- Hannah &amp; Mark</span>
      <span class="quote__mark quote__mark--close">&rdquo;</span>
    </blockquote>

    <footer class="footer-band"><span class="footer-band__web">www.Q85homes.com.au</span></footer>
  </section>

</main>
</body>
</html>
```